QORLIN Business card. A.I. company developing trading strategies.

My name is marcello bianchi and I'm CEO and co-founder of QORLIN Research, an AI company focusing on generating Ai-driven trading strategies.
This is our website: https://qorlin-analytics.example/
Values of our company: tech & R&D driven (we're all very mathy/stats/data driven), sophisticated (we only look for sophisticated, high knowledge investors), reserved (we don't go around telling anyone what we do).
Our main product: PivotFund. A trading strategy that delivered 70% in 2022 and 20% in 2023 so far.
Our main potential clients: HNW individuals, hedge funds, asset managers, tech entrepreneur.
Target Market(s)
Hedge funds, asset managers, High Net Worth individuals, Pension funds
Contact Information for Business Card
The basic: name, job title, company name, address, mail, phone number

```html
<!DOCTYPE html>
<html lang="en">
<head>
<meta charset="utf-8">
<title>QORLIN Research – Business Card</title>
<link rel="stylesheet" href="https://fonts.googleapis.com/css2?family=Poppins:wght@300;400;600;700&display=swap">
<style>
  :root {
    --backdrop: #141517;
    --card-dark: #17181b;
    --card-light: #26272b;
    --accent: #c8183a;
    --ink: #ffffff;
    --deboss: #2c2d31;
  }
  * { box-sizing: border-box; margin: 0; padding: 0; }
  html, body { width: 1200px; height: 1015px; overflow: hidden; }
  body {
    background: var(--backdrop);
    font-family: "Poppins", sans-serif;
    position: relative;
  }
  .card {
    position: absolute;
    width: 640px;
    height: 366px;
    background: linear-gradient(135deg, var(--card-dark) 0%, var(--card-light) 100%);
    overflow: hidden;
    box-shadow: 0 18px 40px rgba(0,0,0,.55);
  }
  .card::after {
    content: "";
    position: absolute;
    left: 0; right: 0; bottom: 0;
    height: 12px;
    background: var(--accent);
  }
  .card--front { left: 120px; top: 90px; }
  .card--back  { left: 440px; top: 540px; }

  .wordmark {
    display: flex;
    align-items: center;
    gap: 10px;
    font-weight: 300;
    letter-spacing: 0.14em;
    line-height: 1;
  }
  .wordmark__dot {
    width: 10px; height: 10px;
    border-radius: 50%;
    background: var(--accent);
  }
  .card--front .wordmark {
    position: absolute;
    left: 50%; top: 46%;
    transform: translate(-50%, -50%);
    font-size: 64px;
    color: var(--deboss);
  }
  .card--back .wordmark {
    position: absolute;
    right: 52px; top: 58px;
    font-size: 48px;
    color: var(--ink);
  }

  .person {
    position: absolute;
    left: 48px; top: 150px;
  }
  .person__name {
    font-weight: 700;
    font-size: 24px;
    line-height: 1;
    color: var(--accent);
    letter-spacing: 0.02em;
  }
  .person__title {
    font-weight: 400;
    font-size: 17px;
    color: var(--ink);
    margin-top: 2px;
  }

  .address {
    position: absolute;
    right: 48px; top: 150px;
    text-align: right;
    font-style: normal;
    font-size: 16px;
    line-height: 1.3;
    color: var(--ink);
  }
  .address__company { color: var(--accent); }

  .contacts {
    position: absolute;
    left: 190px; top: 248px;
    list-style: none;
    font-size: 16px;
    line-height: 1.4;
    color: var(--ink);
  }
  .contacts li { display: flex; align-items: center; gap: 8px; }
  .contacts svg { width: 14px; height: 14px; fill: var(--accent); flex: none; }
  .contacts .highlight { color: var(--accent); }
</style>
</head>
<body>

  <section class="card card--front" aria-label="Business card, front">
    <div class="wordmark"><span>QORLIN</span></div>
  </section>

  <section class="card card--back" aria-label="Business card, back">
    <div class="wordmark"><span>QORLIN</span><span class="wordmark__dot"></span></div>

    <div class="person">
      <p class="person__name">BIANCHI</p>
      <p class="person__title">CEO and Co-founder</p>
    </div>

    <address class="address">
      <div class="address__company">QORLIN Research</div>
      <div>14 Rue des Lanternes</div>
      <div>75011 PARIS 11</div>
    </address>

    <ul class="contacts">
      <li>
        <svg viewBox="0 0 24 24" aria-hidden="true"><path d="M6.6 10.8a15.1 15.1 0 0 0 6.6 6.6l2.2-2.2c.3-.3.7-.4 1-.2 1.1.4 2.3.6 3.6.6.6 0 1 .4 1 1V20c0 .6-.4 1-1 1A17 17 0 0 1 3 4c0-.6.4-1 1-1h3.5c.6 0 1 .4 1 1 0 1.3.2 2.5.6 3.6.1.3 0 .7-.2 1z"/></svg>
        <span>555010294</span>
      </li>
      <li>
        <svg viewBox="0 0 24 24" aria-hidden="true"><path d="M2 5h20v14H2zm2 2v.5l8 5 8-5V7l-8 5z"/></svg>
        <span>office@qorlinresearch.example</span>
      </li>
      <li>
        <svg viewBox="0 0 24 24" aria-hidden="true"><path d="M12 2a10 10 0 1 0 0 20 10 10 0 0 0 0-20zm6.9 6h-3a15 15 0 0 0-1.3-4 8 8 0 0 1 4.3 4zM12 4c.8 1.2 1.5 2.5 1.9 4h-3.8c.4-1.5 1.1-2.8 1.9-4zM4.3 14a8 8 0 0 1 0-4h3.4a16 16 0 0 0 0 4zm.8 2h3a15 15 0 0 0 1.3 4 8 8 0 0 1-4.3-4zm3-8h-3a8 8 0 0 1 4.3-4 15 15 0 0 0-1.3 4zM12 20c-.8-1.2-1.5-2.5-1.9-4h3.8c-.4 1.5-1.1 2.8-1.9 4zm2.3-6H9.7a14 14 0 0 1 0-4h4.6a14 14 0 0 1 0 4zm.3 6a15 15 0 0 0 1.3-4h3a8 8 0 0 1-4.3 4zm1.7-6a16 16 0 0 0 0-4h3.4a8 8 0 0 1 0 4z"/></svg>
        <span>www.<span class="highlight">qorlin-analytics</span>.example</span>
      </li>
    </ul>
  </section>

</body>
</html>
```